Harrowgate Estates Business Card for Apartment Buildings

Create business cards for resident managers who run apartment buildings. The audience is the public who are searching for apartment rentals, and current residents who live at the apartment building. Key design element will be incorporating the company logo, however, the logo cannot dominate. The building name and manager name are more important than the logo. Current business card design leaves little room for copy, so we may need to reduce the size on the current card to allow for more space for copy.

Target Market(s)

Adults 18-65 years of age, who are looking for an apartment rental, plus current residents who live at our apartment buildings.

Industry/Entity Type

Property Management

Contact Information for Business Card

A major design element will be use of the company logo. Important property and manager contact information must be part of the design. The size of the logo will need to be reduced to make room for building and manager contact copy.

Font styles to use
Sans Serif

Colors
3176b5
000000
959595
ffffff

Requirements
Must have
• 1) Incorporate the company logo.
• 2) Use the company colors (dark blue, black/grey, over white).
• 3) FEATURE THE BUILDING NAME
• 4) FEATURE THE MANAGER NAME
• 5) The company name is less important than BUILDING and MANAGER
• 6) Manager contact information
• **SEE ATTACHED CREATIVE BRIEF**
Nice to have
• 1) Back of card logo watermark
• 2) Ability to write notes on back of carfd
Should not have
• Avoid letting the company logo dominate the card, the building name and manager are more important than the company logo.

```html
<!DOCTYPE html>
<html lang="en">
<head>
<meta charset="utf-8">
<title>Harrowgate Estates – Business Card</title>
<link rel="stylesheet" href="https://fonts.googleapis.com/css2?family=Arimo:wght@400;700&display=swap">
<style>
  :root {
    --brand-blue: #1a64a8;
    --ink: #333333;
    --grey: #959595;
    --watermark: #eceef1;
    --paper: #ffffff;
    --backdrop: #e6e6e6;
  }
  * { box-sizing: border-box; margin: 0; padding: 0; }
  html, body {
    width: 970px; height: 1200px; overflow: hidden;
    background: var(--backdrop);
    font-family: "Arimo", Arial, sans-serif;
  }
  .sheet {
    width: 970px; height: 1200px;
    display: flex; flex-direction: column; align-items: center; justify-content: center;
    gap: 110px;
  }
  .card {
    position: relative;
    width: 720px; height: 412px;
    background: var(--paper);
    box-shadow: 0 28px 26px -20px rgba(0,0,0,0.55);
    overflow: hidden;
  }

  /* Back of card */
  .card-back .watermark {
    position: absolute; left: 50%; top: 50%;
    width: 330px; height: 330px; margin: -165px 0 0 -165px;
    border-radius: 50%;
    background: var(--watermark);
  }
  .card-back .company {
    position: absolute; left: 0; right: 0; top: 50%;
    transform: translateY(-50%);
    text-align: center;
    color: var(--brand-blue);
    font-weight: 700;
    font-size: 44px; letter-spacing: 1px; line-height: 1.1;
  }
  .card-back .company span { display: block; font-size: 26px; letter-spacing: 6px; }

  /* Front of card */
  .card-front .band {
    position: absolute; left: 0; right: 0; height: 26px;
    background: var(--brand-blue);
  }
  .card-front .band-top { top: 0; }
  .card-front .band-bottom { bottom: 0; }
  .card-front .company {
    position: absolute; left: 24px; top: 160px; width: 250px;
    text-align: center;
    color: var(--brand-blue); font-weight: 700;
    font-size: 24px; line-height: 1.1; letter-spacing: 0.5px;
  }
  .card-front .company span { display: block; font-size: 14px; letter-spacing: 3px; }
  .card-front .company .dot {
    display: block; width: 38px; height: 38px; margin: 0 auto 10px;
    border-radius: 50%; background: var(--brand-blue);
  }
  .card-front .details {
    position: absolute; left: 318px; top: 62px; right: 20px;
    color: var(--ink);
    white-space: nowrap;
  }
  .building-name {
    color: var(--ink); font-weight: 700;
    font-size: 16px; letter-spacing: 2px; line-height: 1;
    margin-bottom: 10px;
  }
  .manager-name {
    color: var(--brand-blue); font-weight: 700;
    font-size: 33px; letter-spacing: 0.2px; line-height: 1;
  }
  .manager-role { font-size: 24px; color: #555; margin-top: 6px; }
  .address, .contact { font-size: 16px; line-height: 22px; margin-top: 20px; }
  .contact { margin-top: 12px; }
</style>
</head>
<body>
<main class="sheet">
  <section class="card card-back" aria-label="Back of business card">
    <div class="watermark" aria-hidden="true"></div>
    <p class="company">HARROWGATE<span>ESTATES LLC</span></p>
  </section>

  <section class="card card-front" aria-label="Front of business card">
    <div class="band band-top"></div>
    <p class="company"><i class="dot" aria-hidden="true"></i>HARROWGATE<span>ESTATES LLC</span></p>
    <div class="details">
      <p class="building-name">ALDER RIDGE APARTMENTS</p>
      <h1 class="manager-name">DANIEL WHITFORD</h1>
      <p class="manager-role">Property Manager</p>
      <p class="address">2780 Alder Ridge Road #B210<br>Riverton, CA 90215</p>
      <p class="contact">Phone 555-214-7730<br>Fax 555-214-7731<br>daniel@harrowgateestates.us<br>www.harrowgateestates.us</p>
    </div>
    <div class="band band-bottom"></div>
  </section>
</main>
</body>
</html>
```